Coffee bag stamp design for new coffee brand

Stamp design that will be used like a label on a coffee package.
It must be a vector that can be produced as a stamp. Coffee bag is from brown craft paper. I upload image of this bag. Size of design is 80mm x 140mm.
I also uploaded two pictures for inspiration, but I will also appreciate new ideas.

Target Market(s)

Coffee lovers, who love to try new coffee. Also hipsters.

Colors

Designer to choose only greyscale colors for use in the design.

Requirements
Must have
• Some information about coffee must have:
Name: BRAZIL (the biggest font in that design)
Region: Santos
Altitude: 60 – 1200 m.n.m.
Variety: Arabica
Processing: unwashed

```html
<!DOCTYPE html>
<html lang="en">
<head>
<meta charset="utf-8">
<title>Brazil Coffee Stamp</title>
<link rel="stylesheet" href="https://fonts.googleapis.com/css2?family=IBM+Plex+Sans:wght@400;700&display=swap">
<style>
  :root {
    --ink: #000000;
    --paper: #ffffff;
  }
  * { margin: 0; padding: 0; box-sizing: border-box; }
  html, body {
    width: 1200px; height: 1000px; overflow: hidden;
    background: var(--paper);
    font-family: "IBM Plex Sans", Arial, sans-serif;
    color: var(--ink);
  }
  .canvas { position: relative; width: 1200px; height: 1000px; }

  .sunrise { position: absolute; left: 403px; top: 154px; width: 394px; height: 380px; }

  .brand {
    position: absolute; left: 480px; top: 262px; width: 240px;
    text-align: center;
  }
  .brand-name {
    font-weight: 700; font-size: 28px; letter-spacing: 1px; line-height: 1.05;
    text-transform: uppercase;
  }

  .side-bands { position: absolute; left: 403px; top: 530px; width: 394px; height: 320px; }

  .info-card {
    position: absolute; left: 427px; top: 534px; width: 346px; height: 293px;
    border: 1.5px solid var(--ink); background: var(--paper);
  }
  .origin {
    position: absolute; left: 6px; top: 6px; width: 332px; height: 90px;
    background: var(--ink);
    display: flex; align-items: center; justify-content: center;
  }
  .origin h1 { font-weight: 400; font-size: 40px; color: var(--paper); letter-spacing: 0.5px; }
  .row { position: absolute; left: 0; width: 100%; border-top: 1.5px solid var(--ink); }
  .row-details { top: 101px; height: 63px; display: flex; }
  .row-variety { top: 164px; height: 64px; display: flex; align-items: center; justify-content: center; }
  .row-process { top: 228px; height: 63px; }
  .field { flex: 1; padding: 11px 0 0 5px; }
  .field + .field { border-left: 1.5px solid var(--ink); padding-left: 9px; }
  .field-label { font-size: 15px; font-weight: 400; line-height: 1.4; }
  .field-value { font-size: 17px; font-weight: 700; line-height: 1.35; }
  .variety { font-size: 20px; font-weight: 700; letter-spacing: 2.5px; }

  .foot-stripes { position: absolute; left: 470px; top: 828px; width: 115px; height: 18px; }
</style>
</head>
<body>
<div class="canvas">
  <svg class="sunrise" viewBox="0 0 394 380" role="img" aria-label="Sun rising over coffee plants on rolling hills, with dashed rays">
    <rect x="0" y="0" width="394" height="376" fill="var(--ink)"/>
    <circle cx="196" cy="136" r="119" fill="var(--paper)"/>
    <path d="M0 376 Q94 334 194 377 Q300 334 394 376 L394 380 L0 380 Z" fill="var(--paper)"/>
  </svg>

  <div class="brand">
    <p class="brand-name">Kalani<br>Coffee</p>
  </div>

  <svg class="side-bands" viewBox="0 0 394 320" aria-hidden="true">
    <g fill="var(--ink)">
      <path d="M0 24 Q12 18 24 14 L24 24 Q12 28 0 34 Z"/>
      <path d="M0 54 Q12 46 24 40 L24 54 Q12 60 0 68 Z"/>
      <path d="M0 90 Q12 82 24 76 L24 90 Q12 96 0 104 Z"/>
      <path d="M0 126 Q12 120 24 116 L24 130 Q12 134 0 140 Z"/>
      <path d="M0 166 Q12 162 24 160 L24 168 Q12 170 0 176 Z"/>
      <path d="M370 14 Q382 18 394 24 L394 34 Q382 28 370 24 Z"/>
      <path d="M370 40 Q382 46 394 54 L394 66 Q382 58 370 52 Z"/>
      <path d="M370 76 Q382 82 394 92 L394 104 Q382 94 370 88 Z"/>
      <path d="M370 112 Q382 118 394 126 L394 140 Q382 132 370 126 Z"/>
      <path d="M370 226 Q382 230 394 236 L394 248 Q382 242 370 238 Z"/>
      <path d="M370 248 Q382 254 394 262 L394 276 Q382 268 370 262 Z"/>
      <path d="M370 270 Q382 276 394 284 L394 300 Q382 292 370 286 Z"/>
    </g>
  </svg>

  <section class="info-card">
    <div class="origin"><h1>BRAZIL</h1></div>
    <div class="row row-details">
      <div class="field">
        <p class="field-label">Region</p>
        <p class="field-value">SANTOS</p>
      </div>
      <div class="field">
        <p class="field-label">Altitude</p>
        <p class="field-value">60–1200 m.n.m.</p>
      </div>
    </div>
    <div class="row row-variety"><p class="variety">ARABICA</p></div>
    <div class="row row-process">
      <div class="field">
        <p class="field-label">Processing</p>
        <p class="field-value">UNWASHED</p>
      </div>
    </div>
  </section>

  <svg class="foot-stripes" viewBox="0 0 115 18" aria-hidden="true">
    <g fill="var(--ink)">
      <path d="M4 0 H14 L12 18 H0 Z"/>
      <path d="M32 0 H42 L34 18 H24 Z"/>
      <path d="M60 0 H72 L62 18 H52 Z"/>
      <path d="M88 0 H115 L105 18 H78 Z"/>
    </g>
  </svg>
</div>
</body>
</html>
```